Lantern Ridge Tile Inc. Business Card

Looking for business card with embossed raised logo print. Logo provided and want it to be most prominent image on card. Color pallet of black, red, white or charcoal gray preferred for brand recognition. Simple contact information on front and list description of services provided on back. Services included....Custom Showers, Tub Surrounds, Backsplashes, Fireplaces, Floors and more. Dustless Demolition, Lifetime Warranty, Proud member of the Federated Stoneworks Trade Guild

Target Market(s)

High end residential remodel work and new home builders

Contact Information for Business Card

Phone # (402) 555-0193 email address, Lanternridgets@mailvane.net Colby Hanswirth Owner

Requirements
Must have
• Business logo as most prominent image on the front of business card. Along with contact information and name Colby Hanswirth. Would like to see services provided on the back of the card.

```html
<!DOCTYPE html>
<html lang="en">
<head>
<meta charset="utf-8">
<title>Lantern Ridge Tile Inc. Business Card</title>
<link href="https://fonts.googleapis.com/css2?family=Poppins:wght@400;500;600&display=swap" rel="stylesheet">
<style>
  :root {
    --red: #e0232a;
    --black: #0b0b0b;
    --white: #ffffff;
    --charcoal: #2a2a2a;
    --ink: #1a1a1a;
  }
  * { margin: 0; padding: 0; box-sizing: border-box; }
  html, body { width: 1200px; height: 900px; overflow: hidden; }
  body {
    background: var(--charcoal);
    font-family: "Poppins", sans-serif;
    position: relative;
  }
  .card {
    position: absolute;
    left: 262px;
    width: 676px;
    height: 386px;
    border-radius: 22px;
    overflow: hidden;
  }
  .card--services { top: 40px; background: var(--white); }
  .card--contact { top: 474px; background: var(--black); }

  .wordmark {
    display: flex;
    align-items: center;
    gap: 14px;
    color: var(--red);
    font-weight: 600;
    text-transform: uppercase;
    letter-spacing: 1px;
    line-height: 1;
  }
  .wordmark__square { background: var(--red); flex: none; border-radius: 4px; }

  /* services side */
  .card--services .wordmark { position: absolute; left: 44px; top: 46px; font-size: 30px; }
  .card--services .wordmark__square { width: 110px; height: 110px; position: absolute; left: 470px; top: -20px; border-radius: 8px; }
  .services {
    position: absolute; left: 80px; top: 112px;
    list-style: none;
    font-size: 15px; font-weight: 600; color: var(--ink);
    text-transform: uppercase; line-height: 30px;
  }
  .services li { display: flex; align-items: center; gap: 12px; }
  .services li::before {
    content: ""; width: 9px; height: 9px; border-radius: 2px; background: var(--red);
  }
  .strap {
    position: absolute; left: 0; right: 0; bottom: 0;
  }
  .strap__promise {
    height: 44px; background: var(--black); color: var(--white);
    display: flex; align-items: center; justify-content: center; gap: 14px;
    font-size: 15px; font-weight: 500;
  }
  .strap__tick {
    width: 28px; height: 28px; border-radius: 50%; background: var(--red);
    display: flex; align-items: center; justify-content: center;
  }
  .strap__guild {
    height: 42px; background: var(--red); color: var(--white);
    display: flex; align-items: center; justify-content: center;
    font-size: 14px; font-weight: 500; text-transform: uppercase; letter-spacing: .5px;
  }

  /* contact side */
  .card--contact .wordmark {
    position: absolute; left: 0; right: 0; top: 118px; justify-content: center; font-size: 38px;
  }
  .card--contact .wordmark__square { width: 52px; height: 52px; }
  .contact-band {
    position: absolute; left: 0; right: 0; bottom: 0; height: 126px;
    background: var(--red); border-top: 5px solid var(--white);
    display: flex; align-items: center; justify-content: center; gap: 28px;
    color: var(--white);
  }
  .person { text-align: right; }
  .person__name { font-size: 24px; font-weight: 600; text-transform: uppercase; line-height: 1.1; }
  .person__role { font-size: 16px; font-weight: 400; text-transform: uppercase; letter-spacing: 1px; }
  .contact-band__divider { width: 2px; height: 56px; background: var(--white); }
  .reach { list-style: none; font-size: 17px; font-weight: 400; line-height: 30px; }
  .reach li { display: flex; align-items: center; gap: 10px; }
  .reach svg { flex: none; }
</style>
</head>
<body>

<section class="card card--services" aria-label="Card back: services">
  <div class="wordmark"><span>Lantern Ridge Tile Inc.</span><span class="wordmark__square"></span></div>
  <ul class="services">
    <li>Custom Showers</li>
    <li>Tub Surrounds</li>
    <li>Backsplashes</li>
    <li>Fireplaces</li>
    <li>Floors and More</li>
  </ul>
  <div class="strap">
    <div class="strap__promise">
      <span>Dustless Demolition</span>
      <span class="strap__tick">
        <svg width="14" height="12" viewBox="0 0 14 12"><path d="M1 6.5 5 10.5 13 1.5" fill="none" stroke="#fff" stroke-width="2.4" stroke-linecap="round" stroke-linejoin="round"/></svg>
      </span>
      <span>Lifetime Warranty</span>
    </div>
    <div class="strap__guild">Proud Member of the Federated Stoneworks Trade Guild</div>
  </div>
</section>

<section class="card card--contact" aria-label="Card front: contact">
  <div class="wordmark"><span class="wordmark__square"></span><span>Lantern Ridge Tile Inc.</span></div>
  <div class="contact-band">
    <div class="person">
      <div class="person__name">Colby Hanswirth</div>
      <div class="person__role">Owner</div>
    </div>
    <div class="contact-band__divider"></div>
    <ul class="reach">
      <li>
        <svg width="20" height="20" viewBox="0 0 20 20"><rect width="20" height="20" rx="4" fill="#fff"/><path d="M6 4.5c.6 0 1 .3 1.2.8l.8 2c.2.5 0 1-.4 1.3l-.8.6c.7 1.5 1.8 2.6 3.3 3.3l.6-.8c.3-.4.8-.6 1.3-.4l2 .8c.5.2.8.6.8 1.2v1c0 .7-.6 1.2-1.3 1.2C8.5 15.5 4.5 11.5 4.5 6.3c0-.7.5-1.3 1.2-1.3z" fill="#e0232a"/></svg>
        <span>(402) 555-0193</span>
      </li>
      <li>
        <svg width="20" height="20" viewBox="0 0 20 20"><rect width="20" height="20" rx="4" fill="#fff"/><rect x="4" y="6" width="12" height="8.5" fill="none" stroke="#e0232a" stroke-width="1.4"/><path d="M4 6l6 5 6-5M4 14.5l4.5-4M16 14.5l-4.5-4" fill="none" stroke="#e0232a" stroke-width="1.4"/></svg>
        <span>Lanternridgets@mailvane.net</span>
      </li>
    </ul>
  </div>
</section>

</body>
</html>
```